Webdesign für Zirkeltraining für Frauen
Zielgruppe
zirkeltraining für Frauen.
Frauen jeden Alters ... 18-85 Jahre.
Aufgabenstellung
Bitte in den Farben der Bilder und der Logos bleiben. Klare Struktur. Logo wird gerade vom designer Final bearbeitet und liegt daher nur als Beispiel dem Briefing bei.

```html
<!DOCTYPE html>
<html lang="de">
<head>
<meta charset="utf-8">
<title>Lumafit – Unser Blog</title>
<link href="https://fonts.googleapis.com/css2?family=Montserrat:wght@400;500;600&family=Nunito+Sans:wght@400;700;800&display=swap" rel="stylesheet">
<style>
:root{
  --white:#ffffff;
  --ink:#222;
  --accent:#29a9dc;
  --accent-strong:#2196e6;
  --card:#bde0fa;
  --card-light:#dbf0f8;
  --card-mid:#76c9e6;
  --footer:#25acdc;
}
*{box-sizing:border-box;margin:0;padding:0}
html,body{width:711px;height:1200px;overflow:hidden;background:var(--white)}
body{position:relative;font-family:"Nunito Sans",Arial,sans-serif;color:var(--accent)}
.site-header{position:absolute;left:0;top:0;width:711px;height:33px;background:var(--white)}
.brand{position:absolute;left:26px;top:9px;font-family:"Montserrat",sans-serif;font-weight:400;font-size:13px;letter-spacing:3px;color:var(--ink)}
.nav{position:absolute;top:11px;font-family:"Montserrat",sans-serif;font-size:9px;color:var(--ink)}
.nav a{position:absolute;white-space:nowrap;color:inherit;text-decoration:none}
.social{position:absolute;display:flex;gap:9px}
.social span{width:6px;height:6px;border-radius:50%;background:#555}
.hero{position:absolute;left:0;top:33px;width:711px;height:104px;background:linear-gradient(100deg,#6b5446 0%,#b48f6e 30%,#d8bfa2 55%,#9c7a5c 80%,#6a5444 100%)}
.hero h1{position:absolute;left:103px;top:66px;font-family:"Montserrat",sans-serif;font-weight:600;font-size:20px;color:var(--white)}
.card{position:absolute;width:176px;display:flex;flex-direction:column}
.card .body{flex:1;background:var(--card);position:relative;padding:19px 15px 0}
.card .foot{height:46px;display:flex;align-items:center;padding-left:15px;font-weight:800;font-size:7px}
.foot.light{background:var(--card-light);color:var(--accent)}
.foot.mid{background:var(--card-mid);color:var(--white)}
.avatar{width:15px;height:15px;border-radius:50%;background:var(--accent);margin-right:11px;display:flex;align-items:center;justify-content:center}
.meta{display:flex;justify-content:space-between;align-items:center;font-size:4.5px;font-weight:800;text-transform:uppercase;height:8px}
.time{display:flex;align-items:center;gap:4px;font-size:7px;font-weight:400;text-transform:none}
.time i{width:8px;height:8px;border-radius:50%;background:var(--accent-strong);display:block}
.empty .meta{color:var(--white)}
.empty .time i{background:var(--white)}
.title{margin-top:19px;font-weight:800;font-size:7.5px;line-height:11px}
.excerpt{margin-top:35px;font-size:5px;line-height:9px}
.feature{position:absolute;left:81px;top:165px;width:176px;height:445px;background:var(--card-light)}
.feature .top{height:227px;position:relative;padding:37px 15px 0}
.bookmark{position:absolute;right:16px;top:0}
.feature .cat{font-size:4.5px;font-weight:800}
.feature .thumb{margin-top:15px;height:72px;background:#6cc7e4}
.feature .title{margin-top:15px}
.item{height:93px;border-top:1px solid #cde8f3;padding:17px 15px 0}
.item h3{font-size:4.5px;font-weight:800;text-transform:uppercase}
.item h4{margin-top:14px;font-size:7.5px;font-weight:800}
.item p{margin-top:13px;font-size:5px;line-height:9px}
.more{height:31px;border-top:1px solid #cde8f3;text-align:center;font-weight:800;font-size:9px;line-height:22px}
.site-footer{position:absolute;left:0;top:1101px;width:711px;height:99px;background:var(--footer);color:var(--white);font-family:"Montserrat",sans-serif}
.fcol{position:absolute;top:21px}
.fcol h5{font-size:7.5px;font-weight:600;line-height:9px;margin-bottom:9px}
.fcol p{font-size:6px;line-height:7px}
.fcol em{font-style:italic}
.site-footer .social{left:663px;top:27px}
.site-footer .social span{background:var(--white)}
</style>
</head>
<body>
<header class="site-header">
  <div class="brand">LUMAFIT</div>
  <nav class="nav">
    <a style="left:161px">Startseite</a>
    <a style="left:235px">Trainingskonzept</a>
    <a style="left:344px">Mitgliedschaften</a>
    <a style="left:446px">Aktuelles</a>
    <a style="left:515px">Kontakt</a>
  </nav>
  <div class="social" style="left:612px;top:14px" aria-label="Soziale Netzwerke"><span></span><span></span><span></span><span></span></div>
</header>

<section class="hero" role="img" aria-label="Foto: Frauen beim Dehnen auf Yogamatten">
  <h1>Unser Blog</h1>
</section>

<svg width="0" height="0" style="position:absolute"><symbol id="user" viewBox="0 0 10 10"><circle cx="5" cy="3.5" r="1.8" fill="#fff"/><path d="M2 8c0-1.8 1.4-2.6 3-2.6S8 6.2 8 8z" fill="#fff"/></symbol></svg>

<article class="feature">
  <div class="top">
    <svg class="bookmark" width="10" height="21" viewBox="0 0 10 21"><path d="M0 0h10v21l-5-5-5 5z" fill="var(--accent)"/></svg>
    <div class="cat">Ernährung</div>
    <div class="thumb" role="img" aria-label="Beitragsbild"></div>
    <div class="title">Excepteur sint occaecat cupidatat non proident, sunt in culpa qui officia deserunt mollit anim.</div>
  </div>
  <div class="item"><h3>Lorem ipsum</h3><h4>Officia deserunt.</h4><p>Excepteur sint occaecat cupidatat non proident, sunt in culpa qui officia deserunt mollit anim.</p></div>
  <div class="item"><h3>Lorem ipsum</h3><h4>Officia deserunt.</h4><p>Excepteur sint occaecat cupidatat non proident, sunt in culpa qui officia deserunt mollit anim.</p></div>
  <div class="more">...</div>
</article>

<!-- text cards -->
<article class="card" style="left:268px;top:165px;height:212px">
  <div class="body"><div class="meta"><span>Fitness</span><span class="time"><i></i>1h ago</span></div>
  <div class="title">Excepteur sint occaecat cupidatat non proident, sunt in culpa qui officia deserunt mollit anim.</div>
  <div class="excerpt">Excepteur sint occaecat cupidatat non proident, sunt in culpa qui officia deserunt mollit anim.</div></div>
  <div class="foot light"><span class="avatar"><svg width="10" height="10"><use href="#user"/></svg></span>by Name Surname</div>
</article>
<article class="card empty" style="left:268px;top:388px;height:222px">
  <div class="body"><div class="meta"><span>Lorem ipsum</span><span class="time"><i></i>1h ago</span></div></div>
  <div class="foot mid"><span class="avatar"><svg width="10" height="10"><use href="#user"/></svg></span>by Name Surname</div>
</article>
<article class="card empty" style="left:454px;top:165px;height:223px">
  <div class="body"><div class="meta"><span>Lorem ipsum</span><span class="time"><i></i>1h ago</span></div></div>
  <div class="foot mid"><span class="avatar"><svg width="10" height="10"><use href="#user"/></svg></span>by Name Surname</div>
</article>
<article class="card" style="left:454px;top:398px;height:212px">
  <div class="body"><div class="meta"><span>Lorem ipsum</span><span class="time"><i></i>1h ago</span></div>
  <div class="title">Excepteur sint occaecat cupidatat non proident, sunt in culpa qui officia deserunt mollit anim.</div>
  <div class="excerpt">Excepteur sint occaecat cupidatat non proident, sunt in culpa qui officia deserunt mollit anim.</div></div>
  <div class="foot light"><span class="avatar"><svg width="10" height="10"><use href="#user"/></svg></span>by Name Surname</div>
</article>

<article class="card" style="left:81px;top:620px;height:212px">
  <div class="body"><div class="meta"><span>Lorem ipsum</span><span class="time"><i></i>1h ago</span></div>
  <div class="title">Excepteur sint occaecat cupidatat non proident, sunt in culpa qui officia deserunt mollit anim.</div>
  <div class="excerpt">Excepteur sint occaecat cupidatat non proident, sunt in culpa qui officia deserunt mollit anim.</div></div>
  <div class="foot light"><span class="avatar"><svg width="10" height="10"><use href="#user"/></svg></span>by Name Surname</div>
</article>
<article class="card empty" style="left:267px;top:620px;height:223px">
  <div class="body"><div class="meta"><span>Lorem ipsum</span><span class="time"><i></i>1h ago</span></div></div>
  <div class="foot mid"><span class="avatar"><svg width="10" height="10"><use href="#user"/></svg></span>by Name Surname</div>
</article>
<article class="card empty" style="left:451px;top:620px;height:223px">
  <div class="body"><div class="meta"><span>Lorem ipsum</span><span class="time"><i></i>1h ago</span></div></div>
  <div class="foot mid"><span class="avatar"><svg width="10" height="10"><use href="#user"/></svg></span>by Name Surname</div>
</article>

<article class="card empty" style="left:81px;top:843px;height:222px">
  <div class="body"><div class="meta"><span>Lorem ipsum</span><span class="time"><i></i>1h ago</span></div></div>
  <div class="foot mid"><span class="avatar"><svg width="10" height="10"><use href="#user"/></svg></span>by Name Surname</div>
</article>
<article class="card" style="left:267px;top:853px;height:212px">
  <div class="body"><div class="meta"><span>Lorem ipsum</span><span class="time"><i></i>1h ago</span></div>
  <div class="title">Excepteur sint occaecat cupidatat non proident, sunt in culpa qui officia deserunt mollit anim.</div>
  <div class="excerpt">Excepteur sint occaecat cupidatat non proident, sunt in culpa qui officia deserunt mollit anim.</div></div>
  <div class="foot light"><span class="avatar"><svg width="10" height="10"><use href="#user"/></svg></span>by Name Surname</div>
</article>
<article class="card" style="left:451px;top:853px;height:212px">
  <div class="body"><div class="meta"><span>Lorem ipsum</span><span class="time"><i></i>1h ago</span></div>
  <div class="title">Excepteur sint occaecat cupidatat non proident, sunt in culpa qui officia deserunt mollit anim.</div>
  <div class="excerpt">Excepteur sint occaecat cupidatat non proident, sunt in culpa qui officia deserunt mollit anim.</div></div>
  <div class="foot light"><span class="avatar"><svg width="10" height="10"><use href="#user"/></svg></span>by Name Surname</div>
</article>

<footer class="site-footer">
  <div class="fcol" style="left:210px"><h5>Kontakt</h5><p>+49 0000 123456<br>kontakt@lumafit-beispiel.de<br>Lindenweg 12<br>12345 Musterstadt</p></div>
  <div class="fcol" style="left:321px"><h5>Sitelinks</h5><p><em>Das Trainingskonzept<br>Unsere Mitgliedschaften<br>Unser Blog<br>Was ist Zirkeltraining</em></p></div>
  <div class="fcol" style="left:441px"><h5>Informationen /<br>Aktuelles</h5><p>Blogbeitrag 1<br>Blogbeitrag 2<br>Blogbeitrag 3<br>Blogbeitrag 4</p></div>
  <div class="social" aria-label="Soziale Netzwerke"><span></span><span></span><span></span></div>
</footer>
</body>
</html>
```